DL flyer front and back + magnet

DL Flyer Design Brief – DRM Plumbing

Objective:
Create a bold, high-impact DL flyer promoting a Blocked Drain Special to generate immediate service calls.

Main Headline (Large & Eye Catching)

🚨 BLOCKED DRAIN SPECIAL – $299 🚨

High Pressure Water Jetting

Offer Details

💧 Clear stubborn blocked drains fast
💧 Professional high-pressure water jetting
💧 Removes tree roots, grease & debris

Limited Time Bonus

⭐ FIRST 15 CALLS RECEIVE A FREE CCTV CAMERA INSPECTION
(Valued at $149)

Trust Points (Icons or Ticks)

✔ Local Licensed Plumbers
✔ Fast Same Day Service
✔ Upfront Pricing
✔ 5 Star Rated Service

Call To Action (Very Prominent)

📞 CALL NOW TO BOOK
Limited bookings available

Phone: 0417 283 906
Website: drmplumbing.com.au

Branding

Include:

DRM Plumbing logo

Plumbing imagery (blocked drain / jetting hose)

Use brand colours from DRM logo
💡 Design Tip:
The $299 price should be the biggest element on the flyer so people instantly see the offer.

Back Side Layout – DRM Plumbing Flyer
🏠 Your Local Trusted Plumber

Fast, Reliable Plumbing Services Across the Sutherland Shire

We provide professional plumbing services for homes and businesses including:

Our Services

✔ Blocked Drains
✔ Leak Detection & Repairs
✔ Hot Water Systems
✔ Tap & Toilet Repairs
✔ Stormwater Repairs
✔ CCTV Drain Inspections
✔ Gutter & Roof Plumbing
✔ Preventative Plumbing Maintenance

⭐ Why Choose DRM Plumbing?

✔ Fully Licensed & Insured
✔ Upfront Honest Pricing
✔ Fast Local Service
✔ Clean & Professional Workmanship
✔ Trusted by Local Homeowners & Businesses

⭐ What Our Customers Say

⭐⭐⭐⭐⭐
"Lachlan from DRM Plumbing cleared our blocked drain quickly and professionally. Highly recommend!"

⭐⭐⭐⭐⭐
"Prompt, reliable and great service. Will definitely use again."

(Vextra Reviews)

📞 Need a Plumber?

DRM Plumbing

📞 Call: 0417 283 906
🌐 drmplumbing.com.au

Add this small section on the back:

Neighbour Discount

💧 $59 OFF ANY PLUMBING REPAIR
(Mention this flyer when booking)

Magnet should be similar to these

```html
<!DOCTYPE html>
<html lang="en">
<head>
<meta charset="utf-8">
<title>DRM Plumbing – Blocked Drain Special Flyer</title>
<link rel="stylesheet" href="https://fonts.googleapis.com/css2?family=Arimo:wght@400;700&family=Open+Sans:ital,wght@0,400;0,700;1,700&family=Orbitron:wght@900&family=Titillium+Web:ital,wght@0,400;1,700&display=swap">
<style>
  :root {
    --blue: #2dbbe3;
    --yellow: #f5c143;
    --navy: #0d3a52;
    --ink: #1a1a1a;
    --white: #ffffff;
    --page-bg: #6f7076;
    --shirt: #1f2a38;
    --studio: #e9ecef;
  }
  * { box-sizing: border-box; margin: 0; padding: 0; }
  html, body {
    width: 1000px; height: 1200px; overflow: hidden;
    background: var(--page-bg);
  }
  .canvas { position: relative; width: 1000px; height: 1200px; }
  .flyer {
    position: absolute; left: 100px; top: 34px;
    width: 1135px; height: 1605px;
    transform: scale(0.7048); transform-origin: top left;
    background: var(--white); overflow: hidden;
    font-family: "Arimo", Arial, sans-serif;
  }
  .abs { position: absolute; }

  /* Brand */
  .brand {
    left: 55px; top: 95px; display: flex; align-items: center; gap: 18px;
    font-weight: 700; font-size: 64px; color: var(--blue); letter-spacing: 1px;
  }
  .brand-dot { width: 40px; height: 40px; border-radius: 50%; background: var(--yellow); }

  /* Headline */
  .special-band {
    left: 0; top: 268px; width: 657px; height: 150px;
    background: var(--yellow); border-radius: 0 75px 75px 0;
    padding: 18px 0 0 55px;
    font-family: "Orbitron", sans-serif; font-weight: 900;
    font-size: 52px; line-height: 56px; color: var(--white); letter-spacing: 1px;
  }
  .price-band {
    left: 0; top: 418px; width: 505px; height: 138px;
    background: var(--blue); border-radius: 0 69px 69px 0;
    padding-left: 55px;
    font-family: "Orbitron", sans-serif; font-weight: 900;
    font-size: 96px; line-height: 138px; letter-spacing: -8px; color: var(--white);
  }
  .tech-photo {
    left: 638px; top: 22px; width: 497px; height: 590px;
    background: linear-gradient(180deg, var(--studio) 0%, #b9bec6 45%, var(--shirt) 100%);
  }

  /* Blue offer panel */
  .offer-panel { left: 0; top: 612px; width: 1135px; height: 938px; background: var(--blue); }
  .service-tab {
    left: 0; top: 612px; width: 745px; height: 76px;
    background: var(--yellow); border-radius: 0 0 60px 0;
    padding-left: 50px;
    font-weight: 700; font-size: 44px; line-height: 72px; color: var(--navy);
  }
  .splash {
    left: 925px; top: 640px; width: 190px; height: 150px;
    background: radial-gradient(ellipse at 60% 60%, #d8f3fc 0%, #7fd7f2 45%, rgba(45,187,227,0) 72%);
    border-radius: 50%;
  }
  .offer-title {
    left: 52px; top: 722px;
    font-weight: 700; font-size: 45px; color: var(--navy);
  }
  .offer-list { left: 52px; top: 793px; list-style: none; }
  .offer-list li {
    display: flex; align-items: center; gap: 10px;
    font-size: 30px; line-height: 36px; color: var(--white);
  }
  .offer-list svg { width: 16px; height: 20px; flex: none; }
  .job-photo {
    top: 938px; width: 293px; height: 295px;
    border: 3px solid var(--white); border-radius: 10px;
  }
  .job-photo.drain { left: 50px; background: linear-gradient(160deg, #9a9690 0%, #5b5246 50%, #2c2823 100%); }
  .job-photo.pipes { left: 370px; background: linear-gradient(180deg, #6b5448 0%, #7d6153 45%, #5a463c 100%); }

  .bonus-badge {
    left: 685px; top: 722px; width: 368px; height: 366px;
    border-radius: 50%; background: var(--yellow);
    box-shadow: 0 4px 10px rgba(0,0,0,0.25);
    text-align: center; color: var(--ink);
    font-family: "Titillium Web", sans-serif;
    padding-top: 50px;
  }
  .bonus-badge .lead { font-size: 29px; line-height: 38px; }
  .bonus-badge .lead b { font-weight: 700; font-style: italic; }
  .bonus-badge .hero {
    font-weight: 700; font-style: italic; color: var(--navy);
    font-size: 40px; line-height: 46px;
  }
  .bonus-badge .value {
    font-weight: 700; font-style: italic; font-size: 47px; line-height: 58px; margin-top: 4px;
  }
  .bonus-pill {
    left: 705px; top: 1147px; width: 440px; height: 68px;
    background: var(--yellow); border-radius: 34px 0 0 34px;
    text-align: center; padding-right: 12px;
    font-family: "Titillium Web", sans-serif; font-weight: 700; font-style: italic;
    font-size: 40px; line-height: 68px; color: var(--navy);
  }

  /* Trust points */
  .trust-row {
    left: 0; width: 1135px; display: flex; justify-content: center; gap: 44px;
    font-family: "Open Sans", sans-serif; font-size: 34px; color: var(--white);
  }
  .trust-row.first { top: 1268px; }
  .trust-row.second { top: 1325px; gap: 56px; }
  .trust-item { display: flex; align-items: center; gap: 14px; }
  .trust-item svg { width: 34px; height: 34px; }

  /* Call to action */
  .wave { left: 0; top: 1290px; width: 1135px; height: 262px; }
  .cta-text { left: 145px; top: 1450px; font-family: "Open Sans", sans-serif; color: #1b2a33; }
  .cta-text .call { font-weight: 700; font-size: 32px; line-height: 38px; }
  .cta-text .note { font-weight: 700; font-style: italic; font-size: 24px; line-height: 30px; }
  .cta-phone {
    left: 520px; top: 1440px; display: flex; align-items: center; gap: 18px;
    font-family: "Open Sans", sans-serif; font-weight: 700; font-size: 63px; color: var(--navy);
  }
  .cta-phone svg { width: 44px; height: 44px; }
  .site-footer {
    left: 0; top: 1550px; width: 1135px; height: 55px;
    text-align: center; font-size: 22px; line-height: 55px; letter-spacing: 6px; color: var(--ink);
    font-family: "Open Sans", sans-serif;
  }
  .site-footer .domain { color: var(--blue); font-weight: 700; }
</style>
</head>
<body>
<div class="canvas">
  <div class="flyer">
    <div class="abs brand"><span class="brand-dot"></span>DRM Plumbing</div>

    <div class="abs tech-photo" role="img" aria-label="Photo of plumber Lachlan wearing a navy company polo shirt"></div>

    <div class="abs special-band">BLOCKED DRAIN<br>SPECIAL –</div>
    <div class="abs price-band">$299</div>

    <div class="abs offer-panel"></div>
    <div class="abs service-tab">High Pressure Water Jetting</div>
    <div class="abs splash" role="img" aria-label="Water splash droplets"></div>

    <h2 class="abs offer-title">Offer Details</h2>
    <ul class="abs offer-list">
      <li><svg viewBox="0 0 16 20"><path d="M8 0 C8 0 0 10 0 13 a8 7 0 0 0 16 0 C16 10 8 0 8 0Z" fill="var(--navy)"/></svg>Clear stubborn blocked drains fast</li>
      <li><svg viewBox="0 0 16 20"><path d="M8 0 C8 0 0 10 0 13 a8 7 0 0 0 16 0 C16 10 8 0 8 0Z" fill="var(--navy)"/></svg>Professional high-pressure water jetting</li>
      <li><svg viewBox="0 0 16 20"><path d="M8 0 C8 0 0 10 0 13 a8 7 0 0 0 16 0 C16 10 8 0 8 0Z" fill="var(--navy)"/></svg>Removes tree roots, grease &amp; debris</li>
    </ul>

    <div class="abs job-photo drain" role="img" aria-label="Open drain pipe blocked by tree roots"></div>
    <div class="abs job-photo pipes" role="img" aria-label="Copper and PVC pipes along a brick wall"></div>

    <div class="abs bonus-badge">
      <div class="lead">FIRST <b>15 CALLS</b><br>RECEIVE A</div>
      <div class="hero">FREE CCTV CAMERA<br>INSPECTION</div>
      <div class="value">(Valued<br>at $149)</div>
    </div>
    <div class="abs bonus-pill">Limited Time Bonus</div>

    <svg class="abs wave" viewBox="0 0 1135 262" preserveAspectRatio="none" aria-hidden="true">
      <path d="M0 10 Q567 269 1135 22 L1135 262 L0 262 Z" fill="var(--yellow)"/>
    </svg>

    <div class="abs trust-row first">
      <div class="trust-item"><svg viewBox="0 0 34 34"><circle cx="16" cy="18" r="13" fill="none" stroke="var(--navy)" stroke-width="2.5"/><path d="M9 17 l6 7 L31 4" fill="none" stroke="var(--navy)" stroke-width="3" stroke-linecap="round"/></svg>Local Licensed Plumbers</div>
      <div class="trust-item"><svg viewBox="0 0 34 34"><circle cx="16" cy="18" r="13" fill="none" stroke="var(--navy)" stroke-width="2.5"/><path d="M9 17 l6 7 L31 4" fill="none" stroke="var(--navy)" stroke-width="3" stroke-linecap="round"/></svg>Fast Same Day Service</div>
    </div>
    <div class="abs trust-row second">
      <div class="trust-item"><svg viewBox="0 0 34 34"><circle cx="16" cy="18" r="13" fill="none" stroke="var(--navy)" stroke-width="2.5"/><path d="M9 17 l6 7 L31 4" fill="none" stroke="var(--navy)" stroke-width="3" stroke-linecap="round"/></svg>Upfront Pricing</div>
      <div class="trust-item"><svg viewBox="0 0 34 34"><circle cx="16" cy="18" r="13" fill="none" stroke="var(--navy)" stroke-width="2.5"/><path d="M9 17 l6 7 L31 4" fill="none" stroke="var(--navy)" stroke-width="3" stroke-linecap="round"/></svg>5 Star Rated Service</div>
    </div>

    <div class="abs cta-text">
      <div class="call">CALL NOW TO BOOK</div>
      <div class="note">Limited bookings available</div>
    </div>
    <div class="abs cta-phone">
      <svg viewBox="0 0 24 24"><path d="M6.6 10.8a15.1 15.1 0 0 0 6.6 6.6l2.2-2.2a1 1 0 0 1 1-.25 11.4 11.4 0 0 0 3.6.57 1 1 0 0 1 1 1V20a1 1 0 0 1-1 1A17 17 0 0 1 3 4a1 1 0 0 1 1-1h3.5a1 1 0 0 1 1 1c0 1.25.2 2.45.57 3.57a1 1 0 0 1-.25 1z" fill="var(--navy)"/></svg>
      0417 283 906
    </div>

    <div class="abs site-footer">www.<span class="domain">drmplumbing.com</span>.au</div>
  </div>
</div>
</body>
</html>
```